Website for Brisbeck Current Glide

Require a website for a river float in the City of Edmonton. Located on North Saskatchewan River. Will need to be a coded website with incorporated booking system through Fare Harbor software.

Pages include
Home
Pricing
About
FAQ
Contact

Brisbeck Current Glide is an activity based business that will have customers floating down the North Saskatchewan river in Edmonton AB. The site will have all information needed and a full reservation system. The project was launched to provide people in the Edmonton area a favorite summer activity.

Here are similar websites to reference what our business will be doing and what we are looking for.

mellowbendcanoehire.example
pinegulchloopers.example

Target Market(s)

Families, Groups, Individuals, Anyone who wants to explore the river

Industry/Entity Type

Activities based business/ Outdoor recreational/ River Float

Coding

Coded - Design and coding required

Number of Pages Required

5+ page

Colors
0054AA
0677BA
7BADD7
CADEEF
E8F1F8
F0912C
F2A743
F7CA91
FBE8D2
FDF5EE

```html
<!DOCTYPE html>
<html lang="en">
<head>
<meta charset="utf-8">
<title>Brisbeck Current Glide</title>
<link rel="stylesheet" href="https://fonts.googleapis.com/css2?family=Rubik:wght@400;500;700&family=Arimo:wght@400;700&display=swap">
<style>
:root{
  --blue-deep:#0054AA;
  --blue:#0677BA;
  --blue-soft:#7BADD7;
  --blue-pale:#CADEEF;
  --blue-mist:#E8F1F8;
  --cyan:#4EC3E8;
  --navy:#0B3B7C;
  --ink:#333333;
  --grey:#666666;
  --map-fill:#E6ECEA;
  --white:#ffffff;
}
*{box-sizing:border-box;margin:0;padding:0}
html,body{width:1200px;height:3885px;overflow:hidden}
body{position:relative;background:var(--white);font-family:"Arimo",Arial,sans-serif;color:var(--ink)}
h1,h2,h3{font-weight:400}
.btn-outline{position:absolute;display:flex;align-items:center;justify-content:center;border:2px solid var(--blue-deep);border-radius:30px;color:var(--blue-deep);font-family:"Rubik",Arial,sans-serif;font-weight:500;font-size:18px;background:transparent}

/* header */
.site-header{position:absolute;left:0;top:0;width:1200px;height:113px;background:var(--white);border-top:2px solid var(--blue-deep);z-index:3}
.brand-badge{position:absolute;left:113px;top:-40px;width:170px;height:195px;border-radius:50%;background:var(--white);z-index:4;display:flex;align-items:flex-end;justify-content:center;padding-bottom:40px;text-align:center}
.brand-badge span{font-family:"Rubik",Arial,sans-serif;font-weight:700;color:var(--blue-deep);font-size:18px;line-height:1.15}
.main-nav{position:absolute;top:50px;left:0;width:1200px;font-family:"Rubik",Arial,sans-serif;font-weight:500;font-size:15px;color:#222}
.main-nav a{position:absolute;color:inherit;text-decoration:none}
.main-nav a.current{color:var(--blue-deep)}

/* hero */
.hero{position:absolute;left:0;top:113px;width:1200px;height:671px;background:linear-gradient(180deg,#c9dced 0%,#e9e4d6 28%,#b7ae9c 45%,#6f7c58 60%,#4c6a6c 78%,#5f7f3e 100%)}
.hero-title{position:absolute;top:72px;width:100%;text-align:center;font-family:"Rubik",Arial,sans-serif;font-weight:700;font-size:41px;color:var(--blue-deep)}
.hero-sub{position:absolute;top:134px;width:100%;text-align:center;font-family:"Rubik",Arial,sans-serif;font-size:21px;color:#333}
.hero-arrow{position:absolute;top:318px;width:34px;height:34px;border:1.5px solid #333;border-radius:50%;display:flex;align-items:center;justify-content:center}

/* pricing */
.pricing-photo{position:absolute;left:112px;top:843px;width:485px;height:655px;border-radius:0 90px 0 90px;background:linear-gradient(180deg,#a9bfd6 0%,#cfd9e4 38%,#6b5c4c 50%,#3d6c8c 64%,#e9edf0 82%,#cfd6dc 100%)}
.plan-title{position:absolute;left:644px;top:850px;font-family:"Rubik",Arial,sans-serif;font-weight:400;font-size:31px;color:#333}
.plan-price{position:absolute;left:642px;top:900px;font-family:"Rubik",Arial,sans-serif;font-weight:500;font-size:46px;color:var(--blue-deep)}
.plan-price small{font-size:15px;color:#333;font-weight:400}
.plan-copy{position:absolute;left:644px;top:972px;width:440px;font-size:15px;line-height:27px;color:#444}
.plan-list{position:absolute;left:644px;top:1030px;list-style:none}
.plan-list li{height:31.7px;display:flex;align-items:center;font-size:16px;color:#333}
.plan-list svg{margin-right:19px}
.group-box{position:absolute;left:502px;top:1328px;width:586px;height:146px;background:var(--cyan)}
.group-box h3{position:absolute;left:32px;top:46px;font-family:"Rubik",Arial,sans-serif;font-weight:500;font-size:24px;color:var(--white)}
.group-box p{position:absolute;left:30px;top:84px;font-size:14px;color:var(--white)}
.group-box .btn-outline{border-color:var(--white);color:var(--white);left:368px;top:51px;width:180px;height:49px;font-size:17px}

/* about */
.about{position:absolute;left:0;top:1565px;width:1200px;height:597px;background:linear-gradient(100deg,#5cc4ea 0%,#2f9ad6 40%,#0d6bbf 70%,#0a5fb4 100%)}
.about h2{position:absolute;left:112px;top:42px;font-family:"Rubik",Arial,sans-serif;font-weight:400;font-size:40px;color:var(--white)}
.about .rule{position:absolute;left:112px;top:101px;width:42px;height:3px;background:var(--white)}
.about-copy{position:absolute;left:112px;top:117px;width:468px;font-size:13.6px;line-height:28.4px;color:var(--white);text-align:justify}
.about-copy p+p{margin-top:28.4px}
.btn-solid{position:absolute;left:113px;top:499px;width:175px;height:56px;border-radius:30px;background:var(--blue-deep);color:var(--white);display:flex;align-items:center;justify-content:center;font-family:"Rubik",Arial,sans-serif;font-weight:500;font-size:18px}
.about-mark{position:absolute;left:636px;top:56px;width:482px;height:482px;border-radius:50%;background:var(--cyan);border:10px solid #0a3a78;display:flex;align-items:center;justify-content:center;text-align:center}
.about-mark span{font-family:"Rubik",Arial,sans-serif;font-weight:700;font-size:40px;line-height:1.2;color:var(--white)}

/* faq */
.faq{position:absolute;left:0;top:2162px;width:1200px;height:717px;background:linear-gradient(180deg,#f4f8fc 0%,#e9f1f8 55%,#dfeaf3 80%,#f7fafc 100%)}
.faq h2{position:absolute;top:52px;width:100%;text-align:center;font-family:"Rubik",Arial,sans-serif;font-weight:400;font-size:37px;color:var(--blue-deep)}
.faq .rule{position:absolute;left:579px;top:109px;width:41px;height:3px;background:var(--blue-deep)}
.faq-item{position:absolute;left:276px;width:648px;height:56px;background:var(--white);border:2px solid #e2e8ee;border-radius:28px;display:flex;align-items:center;padding-left:20px;font-family:"Rubik",Arial,sans-serif;font-size:15.5px;color:#333}
.faq-item b{font-weight:500;color:var(--blue-deep);font-size:24px;margin-right:8px}
.faq-answer{position:absolute;left:327px;top:214px;width:580px;font-size:13.6px;line-height:26px;color:#666}

/* contact */
.contact h2{position:absolute;left:112px;top:2986px;font-family:"Rubik",Arial,sans-serif;font-weight:400;font-size:39px;color:var(--blue-deep)}
.contact .lede{position:absolute;left:112px;top:3058px;font-family:"Rubik",Arial,sans-serif;font-size:17px;color:#555}
.contact-row{position:absolute;left:111px;display:flex;align-items:center}
.icon-ring{width:50px;height:50px;border-radius:50%;border:2px solid var(--blue-deep);display:flex;align-items:center;justify-content:center;margin-right:17px}
.contact-row .label{font-family:"Rubik",Arial,sans-serif;font-size:14.5px;color:#555;line-height:19px}
.social-dot{position:absolute;width:44px;height:44px;border-radius:50%;border:1.5px solid #999}
.map-panel{position:absolute;left:562px;top:2947px;width:528px;height:502px;border-radius:0 60px 0 60px;border:5px solid #dfe6ee;background:var(--map-fill)}

/* footer */
.site-footer{position:absolute;left:0;top:3512px;width:1200px;height:373px;background:var(--navy);color:var(--white)}
.footer-brand{position:absolute;left:150px;top:42px;width:200px;height:200px;border-radius:50%;border:4px solid var(--white);display:flex;align-items:center;justify-content:center;text-align:center}
.footer-brand span{font-family:"Rubik",Arial,sans-serif;font-weight:700;font-size:24px;line-height:1.2}
.footer-meta{position:absolute;left:131px;top:245px;font-family:"Rubik",Arial,sans-serif;font-size:14.5px;line-height:26px}
.footer-social{position:absolute;width:42px;height:42px;border-radius:50%;border:1.5px solid var(--white);top:308px}
.open-days{position:absolute;left:497px;top:62px;width:220px;text-align:center;font-family:"Rubik",Arial,sans-serif;font-weight:700;font-size:38px;line-height:40px}
.newsletter{position:absolute;left:443px;top:221px;width:344px;height:48px;border:1.5px solid var(--white);border-radius:24px;display:flex;align-items:center;justify-content:space-between;padding:0 20px 0 22px;font-family:"Rubik",Arial,sans-serif;font-size:14.5px}
.copyright{position:absolute;top:296px;left:443px;width:400px;text-align:center;font-family:"Rubik",Arial,sans-serif;font-size:15px}
.footer-nav{position:absolute;left:910px;top:68px;list-style:none;font-family:"Rubik",Arial,sans-serif;font-size:14.5px}
.footer-nav li{height:36px;display:flex;align-items:center}
.footer-nav li::before{content:"»";margin-right:12px;font-size:15px}
</style>
</head>
<body>

<header class="site-header">
  <nav class="main-nav">
    <a class="current" style="left:648px">HOME</a>
    <a style="left:738px">PRICING</a>
    <a style="left:846px">ABOUT</a>
    <a style="left:944px">FAQ</a>
    <a style="left:1019px">CONTACT</a>
  </nav>
</header>
<div class="brand-badge"><span>Brisbeck<br>Current Glide</span></div>

<section class="hero" role="img" aria-label="City skyline above a river valley with a bridge and green banks">
  <h1 class="hero-title">BRISBECK CURRENT GLIDE</h1>
  <p class="hero-sub">FLOAT THE NORTH SASKATCHEWAN THROUGH DOWNTOWN EDMONTON</p>
  <div class="btn-outline" style="left:506px;top:184px;width:186px;height:54px;background:rgba(255,255,255,.35)">BOOK NOW</div>
  <div class="hero-arrow" style="left:67px"><svg width="12" height="12" viewBox="0 0 12 12"><path d="M8 1 3 6l5 5" fill="none" stroke="#333" stroke-width="1.6"/></svg></div>
  <div class="hero-arrow" style="left:1096px"><svg width="12" height="12" viewBox="0 0 12 12"><path d="M4 1l5 5-5 5" fill="none" stroke="#333" stroke-width="1.6"/></svg></div>
</section>

<section class="pricing">
  <div class="pricing-photo" role="img" aria-label="Winter river bend leading toward the downtown skyline"></div>
  <h2 class="plan-title">TUBE AND SHUTTLE</h2>
  <div class="plan-price">$30<small>/PERSON</small></div>
  <div class="btn-outline" style="left:799px;top:905px;width:146px;height:48px;font-size:16px">BOOK NOW</div>
  <p class="plan-copy">We keep our pricing simple and include everything you need :<br>Premium comfort float tube with backrest and cup holder</p>
  <ul class="plan-list">
    <li><svg width="14" height="12" viewBox="0 0 14 12"><path d="M1 6l4 4 8-9" fill="none" stroke="#0054AA" stroke-width="2.6"/></svg>Lifejacket</li>
    <li><svg width="14" height="12" viewBox="0 0 14 12"><path d="M1 6l4 4 8-9" fill="none" stroke="#0054AA" stroke-width="2.6"/></svg>Paddle</li>
    <li><svg width="14" height="12" viewBox="0 0 14 12"><path d="M1 6l4 4 8-9" fill="none" stroke="#0054AA" stroke-width="2.6"/></svg>Round trip shuttle service</li>
    <li><svg width="14" height="12" viewBox="0 0 14 12"><path d="M1 6l4 4 8-9" fill="none" stroke="#0054AA" stroke-width="2.6"/></svg>Safety training</li>
    <li><svg width="14" height="12" viewBox="0 0 14 12"><path d="M1 6l4 4 8-9" fill="none" stroke="#0054AA" stroke-width="2.6"/></svg>Staff assistance</li>
    <li><svg width="14" height="12" viewBox="0 0 14 12"><path d="M1 6l4 4 8-9" fill="none" stroke="#0054AA" stroke-width="2.6"/></svg>Parking</li>
    <li><svg width="14" height="12" viewBox="0 0 14 12"><path d="M1 6l4 4 8-9" fill="none" stroke="#0054AA" stroke-width="2.6"/></svg>Unlimited Fun!</li>
  </ul>
  <div class="btn-outline" style="left:644px;top:1262px;width:147px;height:48px;font-size:16px">BOOK NOW</div>
  <div class="group-box">
    <h3>GROUP OF 10 OR MORE?</h3>
    <p>*does not include taxes or fees</p>
    <div class="btn-outline">CONTACT US</div>
  </div>
</section>

<section class="about">
  <h2>ABOUT US</h2>
  <div class="rule"></div>
  <div class="about-copy">
    <p>Float the North Saskatchewan through downtown Edmonton Edmonton’s Best Summer Activity We provide the lifejacket, paddle, river tube and shuttle service. You just have to show up. Brisbeck Current Glide was launched to provide people in the Edmonton area a favorite summer</p>
    <p>activity. Nothing is better on a hot summer day, than spending it on the river and seeing Edmonton from a new perspective. Our home base and meeting spot is at Willowbank Landing (Map Link), by the Glasshouse Gardens. This is where you will check in, and board the shuttle. The shuttle will take all floaters up river to Cottonwood Park Boat Launch, where your tube will be waiting. Once on the river, you can sit back, relax, explore and enjoy the view. Once you complete the float, and arrive back a close second. Don’t miss out on Edmonton’s best summer activity.</p>
  </div>
  <div class="btn-solid">BOOK NOW</div>
  <div class="about-mark"><span>Brisbeck<br>Current Glide</span></div>
</section>

<section class="faq">
  <h2>OUR FAQ’S</h2>
  <div class="rule"></div>
  <div class="faq-item" style="top:144px"><b>Q.</b>How do I reserve my float?</div>
  <p class="faq-answer">We highly recommend booking online, as we do sell out. BOOK NOW Floats can also be reserved on-site at Willowbank Landing, on a first come first serve basis.</p>
  <div class="faq-item" style="top:294px"><b>Q.</b>What safety information should I know?</div>
  <div class="faq-item" style="top:361px"><b>Q.</b>What is included?</div>
  <div class="faq-item" style="top:430px"><b>Q.</b>What should I bring?</div>
  <div class="faq-item" style="top:498px"><b>Q.</b>Where are you located?</div>
  <div class="faq-item" style="top:566px"><b>Q.</b>What time should I arrive?</div>
</section>

<section class="contact">
  <h2>CONTACT US</h2>
  <p class="lede">We’d love to hear from you!</p>
  <div class="contact-row" style="top:3112px">
    <div class="icon-ring"><svg width="18" height="18" viewBox="0 0 24 24"><path d="M6.6 10.8a15 15 0 0 0 6.6 6.6l2.2-2.2c.3-.3.7-.4 1-.2 1.1.4 2.3.6 3.6.6.6 0 1 .4 1 1V20c0 .6-.4 1-1 1A17 17 0 0 1 3 4c0-.6.4-1 1-1h3.5c.6 0 1 .4 1 1 0 1.3.2 2.5.6 3.6.1.3 0 .7-.2 1z" fill="#0054AA"/></svg></div>
    <div class="label">Phone<br>780XXXXXXX</div>
  </div>
  <div class="contact-row" style="top:3183px">
    <div class="icon-ring"><svg width="18" height="14" viewBox="0 0 18 14"><rect x="1" y="1" width="16" height="12" rx="1.5" fill="none" stroke="#0054AA" stroke-width="1.8"/><path d="M1.5 2 9 8l7.5-6" fill="none" stroke="#0054AA" stroke-width="1.8"/></svg></div>
    <div class="label">Email<br>info@brisbeckcurrentglide.example</div>
  </div>
  <div class="contact-row" style="top:3254px">
    <div class="icon-ring"><svg width="14" height="19" viewBox="0 0 14 19"><path d="M7 0a7 7 0 0 0-7 7c0 5 7 12 7 12s7-7 7-12a7 7 0 0 0-7-7zm0 9.5A2.5 2.5 0 1 1 7 4.5a2.5 2.5 0 0 1 0 5z" fill="#0054AA"/></svg></div>
    <div class="label">Address<br>4120 Ferry Bend Rd NW, Edmonton, AB</div>
  </div>
  <div class="social-dot" style="left:112px;top:3331px"></div>
  <div class="social-dot" style="left:162px;top:3331px"></div>
  <div class="social-dot" style="left:212px;top:3331px"></div>
  <div class="map-panel" role="img" aria-label="Location map of the meeting point beside the river"></div>
</section>

<footer class="site-footer">
  <div class="footer-brand"><span>Brisbeck<br>Current Glide</span></div>
  <div class="footer-meta">EMAIL: info@brisbeckcurrentglide.example<br>LOCATION: Willowbank Landing</div>
  <div class="footer-social" style="left:164px"></div>
  <div class="footer-social" style="left:214px"></div>
  <div class="footer-social" style="left:264px"></div>
  <div class="open-days">7 DAYS<br>A WEEK</div>
  <div class="newsletter"><span>Enter Your Email</span><svg width="16" height="16" viewBox="0 0 16 16"><path d="M15 1 1 7l5 2 2 5z M6 9l9-8" fill="none" stroke="#fff" stroke-width="1.4" stroke-linejoin="round"/></svg></div>
  <p class="copyright">© Copyrights 2022.All Rights Reserved.</p>
  <ul class="footer-nav">
    <li>HOME</li>
    <li>PRICING</li>
    <li>ABOUT</li>
    <li>FAQ</li>
    <li>CONTACT</li>
  </ul>
</footer>

</body>
</html>
```